Whiskey Glass Packaging Design Project

I require a package design for my products - Whiskey Tasting glasses ( Set of 4) I will be selling on the Brevora USA platform. Must be of high quality, something that the customer will be very impressed with after opening once it arrives at their doorstop. To get an idea of competition please take a look on Brevora.com and do a search on Whiskey Glasses - Scotch Glasses. The competition is very good so we require something that will be better than them. We have a home and kitchen brand that caters to an audience that appreciate fine whiskey / oak barrels / cigars ... I can provide logo and content to be placed on box as well as dine line.

Target Market(s)

Men who love all things about Whiskey / Business / Cigars. Men / Women / Wives / Husbands who are looking to buy gifts for Husband / Partner .

Requirements
Must have
• On one side of the box we would like for the following wording to be included.
The KERAVIND snifter glass is one of the ideal glasses that all enthusiasts will swear by. The glass is a type of stemware, a short - stemmed glass whose vessel has a wide bottom and a relatively narrow top. It is mostly used to serve aged brown Scotch / Whiskey, Bourbon and Brandy.
It's simply a matter of raising the glass to take in a whiff of the aromas before taking a sip. We hope the graceful design of this KERAVIND Whiskey glass adds a nice touch of class to the presentation of your favourite drop ! Enjoy !
Nice to have
• Elegant, soothing and relaxing feel.
Should not have
• Nothing aggressive, racist, homosexual / anti gay .

```html
<!DOCTYPE html>
<html lang="en">
<head>
<meta charset="utf-8">
<title>KERAVIND Whiskey Glasses – Box Panels</title>
<link href="https://fonts.googleapis.com/css2?family=Montserrat:wght@300;400&family=Open+Sans:wght@400&family=Cormorant+Garamond:ital,wght@1,400&display=swap" rel="stylesheet">
<style>
  :root {
    --bg: #8a8a8a;
    --panel-white: #f4f4f4;
    --top-fill: #e9e9ea;
    --seam: #b9b9bb;
    --gold-light: #fbf3dc;
    --gold: #d6bc80;
    --gold-deep: #bfa060;
    --ink: #1e1c1c;
    --text-dark: #2b2b2b;
    --logo-gold: #c9a25a;
    --side-text: #4a4a4a;
  }
  html, body { margin: 0; padding: 0; overflow: hidden; }
  body {
    width: 1200px; height: 1200px;
    background: var(--bg);
    position: relative;
    font-family: "Open Sans", sans-serif;
  }
  .top-panel {
    position: absolute; left: 330px; top: 170px;
    width: 810px; height: 250px;
    background: var(--top-fill);
  }
  .top-panel .seam {
    position: absolute; left: 0; right: 0; top: 122px; height: 6px;
    background: var(--seam);
  }
  .side-panel {
    position: absolute; left: 60px; top: 420px;
    width: 270px; height: 500px;
    background: var(--panel-white);
    border-right: 1px solid #dcdcdc;
  }
  .side-logo {
    position: absolute; left: 95px; top: 30px;
    width: 80px; height: 80px; background: var(--ink);
    display: flex; align-items: center; justify-content: center;
  }
  .side-logo span {
    font-family: "Montserrat", sans-serif; font-weight: 300;
    color: var(--logo-gold); font-size: 8px; letter-spacing: 1.5px;
    writing-mode: vertical-rl;
  }
  .side-copy {
    position: absolute; left: 20px; top: 130px;
    width: 230px; height: 350px;
    writing-mode: vertical-rl;
    font-family: "Cormorant Garamond", serif; font-style: italic;
    font-size: 14px; line-height: 1.55; color: var(--side-text);
  }
  .side-copy p { margin: 0 0 0 10px; }
  .front-panel {
    position: absolute; left: 330px; top: 420px;
    width: 810px; height: 500px;
    background: var(--panel-white);
    overflow: hidden;
  }
  .gold-field {
    position: absolute; left: 272px; top: 0; right: 0; bottom: 0;
    background: radial-gradient(ellipse 300px 260px at 300px 200px, #e6d3a2 0%, var(--gold) 55%, var(--gold-deep) 100%);
  }
  .glasses-visual {
    position: absolute; left: 150px; top: 60px;
    width: 310px; height: 320px;
    background: radial-gradient(ellipse closest-side at 50% 45%, var(--gold-light) 0%, rgba(251,243,220,0.6) 45%, rgba(214,188,128,0) 100%);
  }
  .brand-square {
    position: absolute; left: 151px; top: 99px;
    width: 232px; height: 232px;
    background: var(--ink);
    display: flex; flex-direction: column; align-items: center; justify-content: center;
  }
  .brand-square .mark {
    width: 30px; height: 30px; border: 1px solid var(--logo-gold);
    margin-bottom: 18px;
  }
  .brand-square .name {
    font-family: "Montserrat", sans-serif; font-weight: 300;
    color: var(--logo-gold); font-size: 18px; letter-spacing: 3.5px;
  }
  .product-title {
    position: absolute; left: 0; top: 340px; width: 100%; height: 40px;
    margin: 0; font-weight: 400; font-size: 27px; line-height: 40px;
    font-family: "Open Sans", sans-serif;
  }
  .product-title .word-dark {
    position: absolute; right: 543px; color: var(--text-dark);
  }
  .product-title .word-light {
    position: absolute; left: 279px; color: #ffffff;
  }
</style>
</head>
<body>
  <div class="top-panel" role="img" aria-label="Top flaps with a fine light grey repeating pattern">
    <div class="seam"></div>
  </div>

  <section class="side-panel">
    <div class="side-logo"><span>KERAVIND</span></div>
    <div class="side-copy">
      <p>The KERAVIND snifter glass is one of the ideal glasses that all enthusiasts will swear by. The glass is a type of stemware, a short - stemmed glass whose vessel has a wide bottom and a relatively narrow top. It is mostly used to serve aged brown Scotch / Whiskey, Bourbon and Brandy.</p>
      <p>It's simply a matter of raising the glass to take in a whiff of the aromas before taking a sip. We hope the graceful design of this KERAVIND Whiskey glass adds a nice touch of class to the presentation of your favourite drop ! Enjoy !</p>
    </div>
  </section>

  <section class="front-panel">
    <div class="gold-field">
      <div class="glasses-visual" role="img" aria-label="Two clear snifter whiskey glasses with a warm glow behind them, reflected below"></div>
    </div>
    <div class="brand-square">
      <div class="mark"></div>
      <div class="name">KERAVIND</div>
    </div>
    <h1 class="product-title"><span class="word-dark">Whiskey</span><span class="word-light">Glasses</span></h1>
  </section>
</body>
</html>
```